Cloud Software Services Business Needs New Website Design

Our client is looking for a really modern design for their cloud services company. We have a logo, but apart from that, if you read the brief fully and digest the wireframes, we hope you will come up with a really amazing end product.

The design of the website should be professional and trustworthy, it is there to inspire confidence in the services and softwares, as well as emphasising the track record of VRN and relative knowledge and competencies.

Given all the cloud-related communications in the messaging on the site, we will need this in either the imagery or icons in the site so that we can connect the messaging with the service offering.

The brand, being black, gives full range for the designer to present a palette that serves the brand, not forgetting the audience are generally IT decision-makers.

Target Market(s)

Managers and Directors Responsible for IT/Cloud Infrastructure

Industry/Entity Type

IT Technology

Number of Pages Required

5+ page

Font styles to use
Sans Serif

Requirements
Must have
• Initial designs which match the brief and wireframes, focus on the homepage and the winning designer will need to supply the internal pages for the website.
Nice to have
• Clearly considered professional website designs, with consistent design work and branding. If choosing stock imagery, then from PixHarbor Basics please.
Should not have
• Not too much colour, or too consumer/youthful.

```html
<!DOCTYPE html>
<html lang="en">
<head>
<meta charset="utf-8">
<title>VRN – Cloud Services</title>
<link href="https://fonts.googleapis.com/css2?family=Poppins:wght@300;400;500;600&display=swap" rel="stylesheet">
<style>
:root{
  --blue:#1a9fe6;
  --blue-dark:#0f86cc;
  --ink:#1c1c1c;
  --muted:#8a8a8a;
  --grey-band:#f3f3f3;
  --line:#e6e6e6;
  --black:#0b0b0b;
  --white:#ffffff;
}
*{box-sizing:border-box;margin:0;padding:0}
html,body{width:1200px;height:3904px;overflow:hidden}
body{font-family:"Poppins",sans-serif;color:var(--ink);background:var(--white);position:relative}
section,header,footer{position:relative;width:1200px}
.pill{display:inline-block;border:2px solid var(--blue);color:var(--blue);border-radius:20px;font-size:9px;font-weight:500;padding:5px 20px;background:var(--white);white-space:nowrap}
.pill.solid{background:var(--blue);color:var(--white)}
.pill.white{border-color:var(--white);color:var(--blue)}
.pill.ghost{border-color:var(--white);color:var(--white);background:transparent}
.small{font-size:9px;line-height:15px;color:var(--muted)}

/* header */
.site-header{height:109px}
.brand{position:absolute;left:200px;top:36px;font-size:36px;font-weight:500;letter-spacing:1px;color:var(--ink)}
.top-links{position:absolute;right:200px;top:30px;font-size:9px;color:#444;display:flex;gap:14px}
.main-nav{position:absolute;right:200px;top:62px;font-size:10px;font-weight:500;display:flex;gap:44px}
.main-nav .active{color:var(--blue)}

/* hero */
.hero{height:413px;background:
  radial-gradient(ellipse at 22% 40%,rgba(220,120,90,.35),transparent 35%),
  radial-gradient(ellipse at 70% 30%,rgba(190,205,225,.55),transparent 45%),
  linear-gradient(120deg,#26364f 0%,#4f6889 38%,#8fa3c0 62%,#3f5578 100%)}
.hero h1{position:absolute;top:140px;width:100%;text-align:center;color:var(--white);font-weight:400;font-size:34px}
.hero p{position:absolute;top:308px;width:100%;text-align:center;color:var(--white);font-size:13px}
.feature-cards{position:absolute;top:458px;left:0;width:1200px;height:124px;z-index:2}
.feature-card{position:absolute;top:0;width:180px;height:124px;background:var(--white);box-shadow:0 2px 8px rgba(0,0,0,.08);text-align:center;padding-top:24px}
.feature-card svg{width:44px;height:44px}
.feature-card span{display:block;margin-top:12px;font-size:10px;font-weight:600}

/* intro */
.intro{height:440px}
.intro h2{position:absolute;left:200px;top:112px;width:360px;font-size:26px;font-weight:400;line-height:35px}
.intro .copy{position:absolute;left:610px;top:110px;width:390px}
.intro .copy p{margin-bottom:10px}
.ticks{list-style:none;margin-bottom:10px}
.ticks li{position:relative;padding-left:20px;font-size:8.5px;line-height:13px;font-weight:500;color:#333;margin-bottom:4px}
.ticks li:before{content:"";position:absolute;left:2px;top:2px;width:8px;height:4px;border-left:2px solid var(--blue);border-bottom:2px solid var(--blue);transform:rotate(-45deg)}
.intro .cta-line{font-size:9px;font-weight:500;color:#333;margin-bottom:22px}
.intro .cta-line b{color:var(--blue);font-weight:500}

/* blue bands */
.band{background:var(--blue);color:var(--white);text-align:center}
.band .band-brand{font-size:40px;font-weight:400;padding-top:14px;letter-spacing:2px}
.tools{height:325px}
.tools h2{font-size:30px;font-weight:400;margin-top:24px}
.tools h3{font-size:22px;font-weight:300;margin-top:6px}
.tools .pill{margin-top:24px}

/* providers */
.providers{height:302px}
.providers h2{position:absolute;top:56px;width:100%;text-align:center;font-size:22px;font-weight:400}
.provider{position:absolute;top:111px;width:186px;height:125px;background:var(--white);box-shadow:0 1px 6px rgba(0,0,0,.07);text-align:center}
.provider .name{display:block;padding-top:30px;font-size:30px;font-weight:500;color:var(--ink)}
.provider .pill{position:absolute;bottom:-14px;left:50%;transform:translateX(-50%)}
.arrow{position:absolute;top:160px;font-size:20px;color:#555}

/* knowledge */
.knowledge{height:343px;background:var(--grey-band)}
.knowledge h2{position:absolute;left:200px;top:62px;width:400px;font-size:26px;font-weight:400;line-height:34px}
.knowledge .copy{position:absolute;left:200px;top:140px;width:380px}
.knowledge .copy p{margin-bottom:10px}
.photo{position:absolute}
.knowledge .photo{left:610px;top:0;width:390px;height:343px;background:
  radial-gradient(circle at 40% 35%,rgba(120,170,210,.45),transparent 40%),
  radial-gradient(circle at 80% 15%,rgba(240,180,120,.35),transparent 30%),
  linear-gradient(135deg,#2d3646,#6f7e96 50%,#1f2533)}

/* cost */
.cost{height:378px}
.cost .ring{position:absolute;left:200px;top:40px;width:290px;height:290px;border-radius:50%;border:2px solid var(--blue);padding:6px}
.cost .ring .photo{position:relative;width:100%;height:100%;border-radius:50%;background:
  radial-gradient(circle at 70% 30%,rgba(210,180,150,.45),transparent 30%),
  radial-gradient(circle,#5d8ea8,#2f4a5c 70%)}
.cost .badge{position:absolute;left:275px;top:115px;width:140px;height:140px;border-radius:50%;background:rgba(26,159,230,.75);color:var(--white);text-align:center;padding-top:38px}
.cost .badge b{display:block;font-size:32px;font-weight:600;line-height:38px}
.cost .badge span{font-size:11px}
.cost h2{position:absolute;left:610px;top:84px;width:380px;font-size:26px;font-weight:400;line-height:34px}
.cost .copy{position:absolute;left:610px;top:164px;width:390px}
.cost .copy p{margin-bottom:10px}
.cost .copy .lead{font-weight:500;color:#333}

/* get started */
.start{height:294px}
.start h2{font-size:30px;font-weight:400;margin-top:16px}
.start p{font-size:11px;line-height:17px;margin:8px auto 0;width:700px}
.start .actions{margin-top:20px;display:flex;justify-content:center;gap:10px}

/* blog */
.blog{height:541px}
.blog h2{position:absolute;top:52px;width:100%;text-align:center;font-size:24px;font-weight:400}
.post{position:absolute;top:104px;width:250px;text-align:center}
.post .photo{position:relative;width:250px;height:188px}
.post h3{font-size:11px;font-weight:500;line-height:16px;margin-top:18px;padding:0 20px}
.post .small{margin-top:10px;padding:0 15px;font-size:8.5px;line-height:13px}
.post .more{display:inline-block;margin-top:12px;font-size:9px;color:var(--blue);text-decoration:underline}
.blog .view-all{position:absolute;top:436px;left:50%;transform:translateX(-50%)}

/* trusted */
.trusted{height:325px;background:linear-gradient(160deg,#141414,#000 60%,#1a1a1a);color:var(--white)}
.trusted h2{position:absolute;top:48px;width:100%;text-align:center;font-size:32px;font-weight:400}
.client{position:absolute;width:125px;height:72px;background:var(--white);color:#333;font-size:11px;font-weight:500;white-space:nowrap;display:flex;align-items:center;justify-content:center;gap:6px}
.client i{display:inline-block;flex:0 0 10px;width:10px;height:10px;border-radius:50%;background:var(--blue)}

/* footer */
.site-footer{height:416px;background:var(--grey-band)}
.site-footer .brand{left:50%;transform:translateX(-50%);top:10px;font-size:44px}
.col{position:absolute;top:100px}
.col h4{font-size:12px;font-weight:500;margin-bottom:12px}
.col li{list-style:none;font-size:8.5px;color:var(--muted);line-height:17px}
.col .contact li{display:flex;gap:10px;align-items:flex-start;line-height:18px}
.col .contact li svg{margin-top:4px;flex:0 0 10px}
.col .contact li b{color:var(--ink);font-weight:500;font-size:10px}
.col .contact li a{color:var(--blue);text-decoration:underline}
.certs{display:flex;gap:18px;margin-top:14px}
.certs i{display:block;width:54px;height:54px;border-radius:50%;border:3px solid #7ca2c7;background:#dbe6f2}
.certs i.shield{border-radius:6px 6px 26px 26px;background:#1d3f7a;border-color:#1d3f7a}
.legal{position:absolute;top:372px;left:200px;width:800px;font-size:8px;color:var(--muted)}
.legal .links{position:absolute;left:410px;top:0;display:flex;gap:16px}
.legal .up{position:absolute;right:65px;top:-6px;width:0;height:0;border-left:6px solid transparent;border-right:6px solid transparent;border-bottom:14px solid var(--blue)}
</style>
</head>
<body>

<header class="site-header">
  <div class="brand">VRN</div>
  <nav class="top-links"><span>Partners</span><span>|</span><span>Blog</span><span>|</span><span>About Us</span><span>|</span><span>Contact Us</span></nav>
  <nav class="main-nav"><span class="active">Home</span><span>Cloud</span><span>Services</span><span>Software</span></nav>
</header>

<section class="hero" role="img" aria-label="Photo of hands working on a tablet and laptop among charts">
  <h1>Operating Under a Cloud?</h1>
  <p>There's a Silver Lining</p>
</section>

<div class="feature-cards">
  <div class="feature-card" style="left:303px">
    <svg viewBox="0 0 44 44"><path d="M22 3C13 3 6 10 6 19c0 11 16 22 16 22s16-11 16-22C38 10 31 3 22 3z" fill="#1a9fe6"/><circle cx="22" cy="19" r="9" fill="#fff"/><text x="22" y="24" font-size="13" font-weight="600" fill="#1a9fe6" text-anchor="middle" font-family="Poppins,sans-serif">$</text></svg>
    <span>REDUCING COSTS</span>
  </div>
  <div class="feature-card" style="left:511px">
    <svg viewBox="0 0 44 44"><path d="M12 18a8 8 0 0 1 14-6 7 7 0 0 1 10 6 6 6 0 0 1 0 12H12a6 6 0 0 1 0-12z" fill="#1a9fe6"/><rect x="14" y="30" width="16" height="10" rx="2" fill="#1a9fe6"/><path d="M22 20v16M17 31l5 5 5-5" stroke="#fff" stroke-width="2.5" fill="none"/></svg>
    <span>MIGRATION</span>
  </div>
  <div class="feature-card" style="left:717px">
    <svg viewBox="0 0 44 44"><path d="M4 18l10-8 8 4 8-4 10 8-8 10-6 6-4-2-4-2-8-6z" fill="#1a9fe6"/><path d="M14 22l6 5M18 20l6 5M22 18l6 5" stroke="#fff" stroke-width="2"/></svg>
    <span>WORK WITH US</span>
  </div>
</div>

<section class="intro">
  <h2>Did the promise of cloud computing happen for you?</h2>
  <div class="copy">
    <p class="small">We didn't think so! You're not alone. There are many companies just like you who believed in the promise of cloud computing but are now shocked by it.</p>
    <p class="small">But there is a silver lining, which is that VRN have built a business around helping companies improve their cloud efficiencies, reduce costs and simplify their operations as a result.</p>
    <p class="small">It can be summarised in three promises VRN makes to every client or partner:</p>
    <ul class="ticks">
      <li>You can reduce cloud costs, without needing to move supplier</li>
      <li>You can migrate from one cloud to another more easily</li>
      <li>You can simplify your cloud management and choose your favoured provider</li>
    </ul>
    <p class="cta-line">If you already know or want to talk to us just <b>call 01632 960 418</b> or</p>
    <span class="pill">Send an Email</span>
  </div>
</section>

<section class="band tools">
  <div class="band-brand">VRN</div>
  <h2>Your cloud, your tools</h2>
  <h3>A suite of software to simlify deployment</h3>
  <span class="pill white">Cloud Software</span>
</section>

<section class="providers">
  <h2>How hard is it to move your cloud?</h2>
  <span class="arrow" style="left:158px">‹</span>
  <div class="provider" style="left:207px"><span class="name">Stratus</span><span class="pill">View More</span></div>
  <div class="provider" style="left:507px"><span class="name">Nimbly</span><span class="pill solid">View More</span></div>
  <div class="provider" style="left:807px"><span class="name">Cirrova</span><span class="pill">View More</span></div>
  <span class="arrow" style="left:1032px">›</span>
</section>

<section class="knowledge">
  <h2>Knowledgeable independent advice matters</h2>
  <div class="copy">
    <p class="small">Traditionally, the balance of power lies with your host, who has no interest in you moving to another platform. It may also be that your cloud supplier is a linked to your IT firm, developer or even staff preferences and in some cases they will specialise in only one of these suppliers.</p>
    <p class="small">It's time to break free. VRN equips companies, resellers and consultants with the power to choose, to negotiate, to move. We can do this for you.</p>
  </div>
  <div class="photo" role="img" aria-label="Photo of hands typing on a laptop with digital network graphics"></div>
</section>

<section class="cost">
  <div class="ring"><div class="photo" role="img" aria-label="Photo of engineers working in a server room"></div></div>
  <div class="badge"><b>20%</b><span>Cheaper</span></div>
  <h2>Make your cloud costs evaporate</h2>
  <div class="copy">
    <p class="small lead">As cloud costs continue to escalate, and as you suddenly hit new tiers of spend, you may feel helpless in the face of rising costs.</p>
    <p class="small">However, even taking the cost of moving into account, VRN has estimated the average client will save 20% of spend on their cloud by using us to find the best solution and help you to move there.</p>
    <span class="pill" style="margin-top:8px">See Case Study</span>
  </div>
</section>

<section class="band start">
  <div class="band-brand">VRN</div>
  <h2>Let's get started</h2>
  <p>If you would like to speak to a friendly and helpful member of our team, ask questions, discuss option or to help with anything on your mind, please get in touch.</p>
  <div class="actions"><span class="pill white">Call 01632 960 418</span><span class="pill ghost">Send an Email</span></div>
</section>

<section class="blog">
  <h2>VRN latest blog</h2>
  <article class="post" style="left:200px">
    <div class="photo" role="img" aria-label="Photo of orange network cables in a data centre" style="background:radial-gradient(circle at 40% 45%,#f08a2a,transparent 45%),linear-gradient(135deg,#1f2a36,#c0651d 50%,#2f2418)"></div>
    <h3>Lorem Ipsum is simply dummy text of the printing</h3>
    <p class="small">It is a long established fact that a reader will be distracted by the readable content of a page when looking at its layout.</p>
    <span class="more">Read More</span>
  </article>
  <article class="post" style="left:475px">
    <div class="photo" role="img" aria-label="Photo of a woman holding a phone beside a blue cloud shape" style="background:radial-gradient(ellipse at 55% 80%,#2f97d6,transparent 45%),linear-gradient(160deg,#cdb898,#9fb0bb 55%,#4d8fb8)"></div>
    <h3>Lorem Ipsum is simply dummy text of the printing</h3>
    <p class="small">It is a long established fact that a reader will be distracted by the readable content of a page when looking at its layout.</p>
    <span class="more">Read More</span>
  </article>
  <article class="post" style="left:750px">
    <div class="photo" role="img" aria-label="Illustration of a glowing cloud over a digital city" style="background:radial-gradient(circle at 50% 45%,#eef3f8,#6d8aa8 40%,#1e2f45)"></div>
    <h3>Lorem Ipsum is simply dummy text of the printing</h3>
    <p class="small">It is a long established fact that a reader will be distracted by the readable content of a page when looking at its layout.</p>
    <span class="more">Read More</span>
  </article>
  <span class="pill view-all">View All</span>
</section>

<section class="trusted">
  <h2>Trusted by</h2>
  <div class="client" style="left:200px;top:130px"><i></i>Company Name</div>
  <div class="client" style="left:335px;top:130px">Northlane</div>
  <div class="client" style="left:470px;top:130px"><i></i>Greyfield</div>
  <div class="client" style="left:605px;top:130px"><i></i>Company Name</div>
  <div class="client" style="left:740px;top:130px">Northlane</div>
  <div class="client" style="left:875px;top:130px"><i></i>Company Name</div>
  <div class="client" style="left:402px;top:216px"><i></i>Greyfield</div>
  <div class="client" style="left:537px;top:216px">Northlane</div>
  <div class="client" style="left:672px;top:216px"><i></i>Greyfield</div>
</section>

<footer class="site-footer">
  <div class="brand">VRN</div>
  <div class="col" style="left:200px">
    <h4>Cloud Services</h4>
    <ul><li>Stratus</li><li>Nimbly</li><li>Cirrova</li><li>Orvane</li><li>Kelvar</li><li>Tidecloud</li><li>Others</li><li>Private Cloud</li></ul>
  </div>
  <div class="col" style="left:405px">
    <h4>Services</h4>
    <ul><li>Cloud Cost Review</li><li>Migration Planning</li><li>Migration Execution</li><li>Security &amp; Compliance</li></ul>
    <h4 style="margin-top:22px">Software</h4>
    <ul><li>Skyport</li><li>Shiftwell</li></ul>
  </div>
  <div class="col" style="left:610px">
    <h4>About VRN</h4>
    <ul><li>Blog</li><li>Partner</li><li>About Us</li><li>Contact Us</li></ul>
    <div class="certs"><i></i><i class="shield"></i></div>
  </div>
  <div class="col" style="left:815px">
    <h4>Connect</h4>
    <ul class="contact">
      <li><svg width="10" height="10" viewBox="0 0 10 10"><path d="M2 1l2 2-1 1.5c.6 1.2 1.3 1.9 2.5 2.5L7 6l2 2-1.5 1.5C4 9 1 6 .5 2.5z" fill="#1a9fe6"/></svg><b>01632 960 418</b></li>
      <li><svg width="10" height="10" viewBox="0 0 10 10"><rect x="0" y="2" width="10" height="7" fill="#1a9fe6"/><path d="M0 2l5 4 5-4" stroke="#fff" fill="none"/></svg><a>Email Us</a></li>
      <li><svg width="10" height="10" viewBox="0 0 10 10"><rect width="10" height="10" rx="1" fill="#1a9fe6"/></svg><a>Social</a></li>
      <li><svg width="10" height="10" viewBox="0 0 10 10"><path d="M5 0a3.5 3.5 0 0 1 3.5 3.5C8.5 6 5 10 5 10S1.5 6 1.5 3.5A3.5 3.5 0 0 1 5 0z" fill="#1a9fe6"/></svg><span style="font-size:8.5px;color:#333">Address<br><span style="color:#8a8a8a;line-height:12px;display:block">Skyline House, Mill Road<br>Ashford, TN9 4QX<br>England</span></span></li>
    </ul>
  </div>
  <div class="legal">
    © 2021 <span style="color:#1a9fe6">VRN</span>. All Rights Reserved.
    <div class="links"><span>Sitemap</span><span>Terms of Use</span><span>Privacy Policy</span><span>Contact Us</span></div>
    <span class="up"></span>
  </div>
</footer>

</body>
</html>
```